Pitch book for Birchvale Real Estate Investors.

Birchvale Investors is a new real estate investment company focused on multifamily (apartment) investments along the San Francisco Peninsula (in other parts of the world it is also referred to as flats). We need a professional Pitch Book i.e. brochure (digital and print) to raise equity from private investors. Read about “pitch book” on Wikipedia. The profile of the investor is conservative and must qualify as an accredited investor. Think high net worth individuals, CEOs and wealthy retiring couples. The investor that is attracted to real estate invest because it is low risk, produce cash flow and provide solid returns over the long term.

The brochure should convey trust, be highly professional and be clean and crisp. I attach a PowerPoint doc to be used as a copy for the brochure. I also attach a brochure of Harlow Pike – I like the look and feel, think it was designed with InDesign.

We will use the brochure at one-on-one meetings with investors where we will present on a laptop; we also need it in a format so that we can email it, print it and use it to be uploaded as a website.

I prefer the up and down scroll format (like you would do on a Mac) compared to PowerPoint but I am open to suggestions.

The photos I used in the PowerPoint presentation was found on the web, please use your own stock images.

Target Market(s)

High net worth individuals

Industry/Entity Type

Real Estate

Font styles to use
Serif

Requirements
Must have
• See attached Power Point
Nice to have
• See attached HPK brochure, I like the look and feel.
Should not have
• I am open to your ideas.

```html
<!DOCTYPE html>
<html lang="en">
<head>
<meta charset="utf-8">
<title>Birchvale — Acquisition Process</title>
<link href="https://fonts.googleapis.com/css2?family=Courier+Prime:wght@700&family=Open+Sans:ital,wght@0,400;0,600;0,700;1,400&display=swap" rel="stylesheet">
<style>
:root{
  --blue:#2f5fb3;
  --ink:#111111;
  --text:#222222;
  --paper:#ffffff;
  --photo-a:#2b3a55;
  --photo-b:#c9cfd8;
}
*{margin:0;padding:0;box-sizing:border-box}
html,body{width:865px;height:1200px;overflow:hidden;background:var(--paper)}
.page{position:relative;width:865px;height:1200px;background:var(--paper);font-family:"Open Sans",Arial,sans-serif;color:var(--text)}
.header-brand{position:absolute;left:52px;top:6px;font-weight:700;font-size:16px;letter-spacing:1.5px;color:var(--ink);display:flex;align-items:center;gap:6px}
.header-brand .mark{width:9px;height:9px;background:var(--ink)}
.header-title{position:absolute;left:287px;top:6px;font-size:15px;letter-spacing:.5px;color:var(--ink)}
.header-rule{position:absolute;left:474px;top:44px;width:391px;height:4px;background:var(--blue)}
.photo{position:absolute;left:0;top:86px;width:432px;height:1047px;background:linear-gradient(160deg,var(--photo-b) 0%,#8a93a3 35%,var(--photo-a) 100%)}
.content{position:absolute;left:476px;top:86px;width:340px}
.section-title{font-family:"Courier Prime","Courier New",monospace;font-weight:700;font-size:33px;line-height:30px;color:var(--blue);letter-spacing:.5px}
.lead{margin-top:26px;font-weight:700;font-size:20px;line-height:28px;color:var(--ink);text-align:justify}
.steps-label{margin-top:28px;font-weight:700;font-size:20px;color:var(--text)}
.steps{list-style:none;margin-top:16px}
.steps li{font-style:italic;font-size:24px;line-height:35px;color:var(--text);padding-bottom:10px}
.steps li + li{border-top:4px solid var(--blue);padding-top:14px;width:100%}
.steps li + li{border-image:linear-gradient(to right,var(--blue) 0,var(--blue) 253px,transparent 253px) 1}
.footer-mark{position:absolute;left:52px;top:1175px;width:11px;height:11px;background:var(--ink)}
.footer-title{position:absolute;left:330px;top:1172px;font-size:14px;letter-spacing:.5px;color:var(--ink)}
.page-number{position:absolute;left:800px;top:1170px;font-weight:700;font-size:15px;color:var(--ink)}
</style>
</head>
<body>
<div class="page">
  <div class="header-brand">BIRCHVALE <span class="mark"></span></div>
  <div class="header-title">MULTIFAMILY REAL ESTATE INVESTMENT</div>
  <div class="header-rule"></div>

  <div class="photo" role="img" aria-label="Smiling businessman in a suit reviewing documents with a colleague"></div>

  <div class="content">
    <h1 class="section-title">ACQUISITION<br>PROCESS</h1>
    <p class="lead">Finding the right opportunity is one of the most critical factors that will contribute to the success of a real estate investment company.</p>
    <p class="steps-label">Acquisition process steps:</p>
    <ul class="steps">
      <li>Maintain accurate data base of properties and property owners</li>
      <li>Implement our CMU program – call, meet and uncover opportunity</li>
      <li>Build long-term relationships with owners and brokers</li>
      <li>Implement continuous touch point program Network at property owner and property manager forums</li>
      <li>Protect broker commissions for off-market opportunities</li>
    </ul>
  </div>

  <div class="footer-mark"></div>
  <div class="footer-title">SAN FRANCISCO PENINSULA</div>
  <div class="page-number">1</div>
</div>
</body>
</html>
```